Design a nice single page website containing a link list

Hello,

you should design a nice single page website to replace the old website http://www.tovrella.de/

The company is running multiple flag shops. Your new website should only lead to a lot of other company websites. They are mentioned below. No link dropdowns please. We would like to see all links.

The company is offering flags. Big flags, but the special products are high quality diplomatic car flags. It is important, that people see, that it is about flags and specialy about car flags.

As customers are very international, the website should not contain unnecessary text. No text, no wrong languages.

You should implement links to:

Car Flag Shops: (pleaae don't use this as headline. Use symbols)
New Logo: Little car attached (without text below)
http://www.ridepennon.eu (english site payment in Euro)
http://us.ridepennon.eu (english site payment in USD)
http://fr.ridepennon.eu (french site payment in Euro)
http://es.ridepennon.eu (spanish site payment in Euro)
http://de.ridepennon.eu (germansite payment in Euro)

http://www.ridepennon.net (english site payment in USD)
http://www.ridepennant.co.uk (english site payment in british pounds)
http://www.wagen-wimpel.net (german site payment in Euro)
http://www.wagen-banner.at (austrian site payment in Euro)
http://www.wagen-wimpl.ch (german site payment in Swiss Franken)

Big flag shops: (pleaae don't use this as headline. Use symbols)
Logo: tovRella (attached incl. font) (black part of logo can also be made white)
(World map used next to the tovRella font attached)
http://www.tovrella.ne/ (english site payment in Euro)
http://fr.tovrella.net (french site payment in Euro)
http://es.tovrella.net (spanish site payment in Euro)
http://de.tovrella.net (german site payment in Euro)
http://it.tovrella.net (italian site payment in Euro)

Car flags product page: (pleaae don't use this as headline. Use symbols)
Logo: EnvoyPennon (attached incl. font)
http://www.envoy-pennon.com (english site)
http://fr.envoy-pennon.com (french site)
http://es.envoy-pennon.com (spanish site)
http://de.envoy-pennon.com (german site)

Please also add links to
English Blog
German Blog
4 language newsletter registration forms.

Also company data has to be added to the bottom of the page.
You could copy / paste from here:
http://www.ridepennon.eu/tovRella-GmbH

No additional links. No social icons.

General design:
Customers are, ambassoders, embassies, international organisiations.
Customers are powerful men, who want to show their power.
That's the reason, why they add this car flags to their car.

So colors should not be too soft. In the past we used colors like black and gold.
Completly black / dark background and bright white text is ok.

Most of our company prints have the kelvane arch in the background.
It would be good to include this also. (Image attached)

It is about a flag company. So don't forget to add big flags.
It would be also good to include an image like this:
http://de.pixvendra.com/id/38275016

Logos are available in high resolution. At the end you should mail us psd file with your winning design.

Please feel free to use all images you will find on the websites above.
If you need special images, please let me know, and we willt try to provide them.

Kind regards,

Dorian
Updates

Hello,
thanks for your feedback.Project payment is now committed.
Kind regards,
Lorenzo

Target Market(s)

World wide

Industry/Entity Type

Flag

Requirements
Must have
• Self explaining links to all the target pages.
Should not have
• unnecessary text. Domain names and logos with text are fine.
I think, we could avoid nearly all other text.

```html
<!DOCTYPE html>
<html lang="en">
<head>
<meta charset="utf-8">
<title>tovRella – Diplomatic Car Flags</title>
<link href="https://fonts.googleapis.com/css2?family=Lato:wght@400;700&display=swap" rel="stylesheet">
<style>
:root{
  --navy:#0a1a33;
  --ink:#0f2340;
  --gold:#8a7130;
  --line:#d6d6d6;
  --muted:#777;
  --footer:#262626;
  --footer-text:#9a9a9a;
  --band:#f0f0f0;
  --head-band:#f7f7f7;
}
*{box-sizing:border-box;margin:0;padding:0}
html,body{width:879px;height:1200px;overflow:hidden}
body{font-family:'Lato',Arial,sans-serif;background:#fff;color:#333;position:relative}
a{text-decoration:none;color:inherit}

.site-header{position:absolute;left:0;top:0;width:879px;height:55px;background:var(--navy)}
.brand{position:absolute;left:118px;top:12px;font-size:27px;font-weight:700;color:#fff;letter-spacing:.5px}
.blog-nav{position:absolute;right:117px;top:23px;font-size:10.5px;color:#fff}
.blog-nav a{margin-left:14px}

.hero{position:absolute;left:0;top:55px;width:879px;height:324px;background:linear-gradient(180deg,#ececec,#e2e2e2)}
.hero-map{position:absolute;inset:0}
.hero-title{position:absolute;left:131px;top:128px;font-size:30px;line-height:36px;font-weight:700;color:var(--ink)}
.video{position:absolute;left:413px;top:57px;width:358px;height:228px;background:#1a1a1a;box-shadow:0 4px 10px rgba(0,0,0,.35)}
.video-still{position:absolute;left:2px;top:2px;width:354px;height:197px;background:linear-gradient(90deg,#6b5e3e,#2a2418 40%,#2a2418 60%,#6b5e3e)}
.video-play{position:absolute;left:174px;top:92px}
.video-bar{position:absolute;left:0;top:200px;width:358px;height:28px;background:linear-gradient(#2d3a4a,#141b24)}
.time{position:absolute;top:9px;font-size:8px;color:#cfe0f5}

.finder{position:absolute;left:0;top:379px;width:879px;height:46px;background:var(--band)}
.finder-label{position:absolute;left:117px;top:17px;font-size:11px;color:#555}
.finder-input{position:absolute;left:221px;top:11px;width:300px;height:26px;background:#fff;border:1px solid var(--line);font-size:10px;color:#bbb;padding:7px 14px}
.finder-pin{position:absolute;right:0;top:0;width:26px;height:24px;border-left:1px solid var(--line)}
.finder-btn{position:absolute;left:536px;top:11px;width:117px;height:26px;background:var(--gold);color:#fff;font-size:11px;font-weight:700;text-align:center;line-height:26px}
.advanced{position:absolute;left:665px;top:18px;font-size:10px;color:#333}

.panel{position:absolute;border:1px solid var(--line);background:#fff}
.panel-band{height:37px;border-bottom:1px solid var(--line);background:var(--head-band)}
.panel-mark{height:50px;display:flex;align-items:center;justify-content:center}
.links{list-style:none;padding-left:8px}
.links li{position:relative;padding-left:17px;height:35.5px}
.links li svg{position:absolute;left:0;top:3px}
.links a{display:block;font-size:11px;color:var(--ink);line-height:12px}
.links small{display:block;font-size:8.5px;color:var(--muted);line-height:10px}
.mark-text{font-size:21px;font-weight:700;color:#1a1a1a}
.mark-text.gold{color:var(--gold);font-size:18px}
.car-area{width:104px;height:34px;background:linear-gradient(#fafafa,#e4e4e4);border-radius:10px}

.newsletter{position:absolute;left:557px;top:448px;width:205px;height:380px;border:1px solid var(--line)}
.news-head{height:37px;background:var(--gold);color:#fff;font-size:13px;text-align:center;line-height:37px}
.news-intro{font-size:8.5px;line-height:12px;color:#333;padding:8px 9px;height:46px;border-bottom:1px solid var(--line)}
.lang{position:relative;height:38.5px;border-bottom:1px solid var(--line);font-size:9px;color:#222;padding:13px 0 0 28px}
.lang .flag{position:absolute;left:10px;top:14px;width:11px;height:8px}
.lang .chev{position:absolute;right:6px;top:11px}
.lang.open{height:148px;padding-top:5px}
.lang.open .flag{top:6px}
.lang.open .chev{top:3px}
.field-label{position:absolute;left:10px;font-size:9px;color:#333}
.field{position:absolute;left:10px;width:177px;height:20px;border:1px solid var(--line)}
.send{position:absolute;left:65px;top:120px;width:75px;height:17px;background:var(--gold);color:#fff;font-size:9px;font-weight:700;text-align:center;line-height:17px}
.news-note{font-size:7.5px;color:var(--muted);line-height:10px;padding:5px 9px}

.site-footer{position:absolute;left:0;top:968px;width:879px;height:232px;background:var(--footer);color:var(--footer-text)}
.foot-col{position:absolute;top:16px;font-size:9.5px;line-height:13.6px}
.foot-col h3{font-size:11px;font-weight:400;color:#fff;margin-bottom:8px}
.foot-col ul{list-style:none}
.foot-col li::before{content:"•";color:var(--gold);margin-right:8px}
.divider{position:absolute;top:30px;width:1px;height:150px;background:#303030}
.foot-rule{position:absolute;left:117px;top:178px;width:645px;height:3px;background:#1b1b1b}
.foot-legal{position:absolute;left:0;top:192px;width:879px;text-align:center;font-size:8.5px;line-height:13px;color:#7a7a7a}
</style>
</head>
<body>

<header class="site-header">
  <a class="brand" href="#">tovRella</a>
  <nav class="blog-nav"><a href="#">English Blog</a><a href="#">German Blog</a></nav>
</header>

<section class="hero">
  <div class="hero-map" role="img" aria-label="Street map background"></div>
  <h1 class="hero-title">High Quality<br>Diplomatic Car Flags</h1>
  <div class="video">
    <div class="video-still" role="img" aria-label="Video still of an embassy gate with national crests"></div>
    <svg class="video-play" width="12" height="14"><path d="M0 0L12 7L0 14Z" fill="#fff"/></svg>
    <div class="video-bar">
      <svg width="358" height="28">
        <path d="M11 9L19 14L11 19Z" fill="#fff"/>
        <rect x="39" y="10" width="193" height="7" rx="3.5" fill="#0d1118"/>
        <rect x="39" y="10" width="125" height="7" rx="3.5" fill="#3b8fd8"/>
        <circle cx="164" cy="13.5" r="5" fill="#e8e8e8"/>
        <path d="M296 11h3l4-3v12l-4-3h-3z" fill="#fff"/>
        <g fill="#bcd8f3"><rect x="311" y="10" width="2" height="7"/><rect x="315" y="10" width="2" height="7"/><rect x="319" y="10" width="2" height="7"/><rect x="323" y="10" width="2" height="7"/><rect x="327" y="10" width="2" height="7"/></g>
      </svg>
      <span class="time" style="left:240px">3:05</span>
      <span class="time" style="left:261px">4:36</span>
    </div>
  </div>
</section>

<section class="finder">
  <span class="finder-label">Find Your Flags</span>
  <div class="finder-input">Your location
    <span class="finder-pin"><svg width="26" height="24"><circle cx="13" cy="12" r="5" fill="none" stroke="#aaa"/><circle cx="13" cy="12" r="1.8" fill="#aaa"/></svg></span>
  </div>
  <a class="finder-btn" href="#">Find Flags Near You</a>
  <span class="advanced">Advanced Search</span>
  <svg style="position:absolute;left:746px;top:18px" width="14" height="14"><circle cx="7" cy="7" r="6" fill="none" stroke="#8a7130"/><path d="M4 6l3 3 3-3" fill="none" stroke="#8a7130"/></svg>
</section>

<section class="panel" aria-label="Car flag shops" style="left:116px;top:448px;width:204px;height:451px">
  <div class="panel-band"></div>
  <div class="panel-mark"><div class="car-area" role="img" aria-label="Car with flag outline"></div></div>
  <ul class="links">
    <li><svg width="11" height="11"><circle cx="5.5" cy="5.5" r="5" fill="none" stroke="#aaa"/><path d="M.5 5.5h10M5.5.5c-3 3-3 7 0 10M5.5.5c3 3 3 7 0 10" fill="none" stroke="#aaa"/></svg><a href="#">http://www.ridepennon.eu</a><small>(english site payment in Euro)</small></li>
    <li><svg width="11" height="11"><circle cx="5.5" cy="5.5" r="5" fill="none" stroke="#aaa"/><path d="M.5 5.5h10M5.5.5c-3 3-3 7 0 10M5.5.5c3 3 3 7 0 10" fill="none" stroke="#aaa"/></svg><a href="#">http://us.ridepennon.eu</a><small>(english site payment in USD)</small></li>
    <li><svg width="11" height="11"><circle cx="5.5" cy="5.5" r="5" fill="none" stroke="#aaa"/><path d="M.5 5.5h10M5.5.5c-3 3-3 7 0 10M5.5.5c3 3 3 7 0 10" fill="none" stroke="#aaa"/></svg><a href="#">http://fr.ridepennon.eu</a><small>(french site payment in Euro)</small></li>
    <li><svg width="11" height="11"><circle cx="5.5" cy="5.5" r="5" fill="none" stroke="#aaa"/><path d="M.5 5.5h10M5.5.5c-3 3-3 7 0 10M5.5.5c3 3 3 7 0 10" fill="none" stroke="#aaa"/></svg><a href="#">http://es.ridepennon.eu</a><small>(spanish site payment in Euro)</small></li>
    <li><svg width="11" height="11"><circle cx="5.5" cy="5.5" r="5" fill="none" stroke="#aaa"/><path d="M.5 5.5h10M5.5.5c-3 3-3 7 0 10M5.5.5c3 3 3 7 0 10" fill="none" stroke="#aaa"/></svg><a href="#">http://de.ridepennon.eu</a><small>(germansite payment in Euro)</small></li>
    <li><svg width="11" height="11"><circle cx="5.5" cy="5.5" r="5" fill="none" stroke="#aaa"/><path d="M.5 5.5h10M5.5.5c-3 3-3 7 0 10M5.5.5c3 3 3 7 0 10" fill="none" stroke="#aaa"/></svg><a href="#">http://www.ridepennon.net/</a><small>(english site payment in USD)</small></li>
    <li><svg width="11" height="11"><circle cx="5.5" cy="5.5" r="5" fill="none" stroke="#aaa"/><path d="M.5 5.5h10M5.5.5c-3 3-3 7 0 10M5.5.5c3 3 3 7 0 10" fill="none" stroke="#aaa"/></svg><a href="#">http://www.ridepennant.co.uk</a><small>(english site payment in british pounds)</small></li>
    <li><svg width="11" height="11"><circle cx="5.5" cy="5.5" r="5" fill="none" stroke="#aaa"/><path d="M.5 5.5h10M5.5.5c-3 3-3 7 0 10M5.5.5c3 3 3 7 0 10" fill="none" stroke="#aaa"/></svg><a href="#">http://www.wagen-wimpel.net</a><small>(german site payment in Euro)</small></li>
    <li><svg width="11" height="11"><circle cx="5.5" cy="5.5" r="5" fill="none" stroke="#aaa"/><path d="M.5 5.5h10M5.5.5c-3 3-3 7 0 10M5.5.5c3 3 3 7 0 10" fill="none" stroke="#aaa"/></svg><a href="#">http://www.wagen-banner.at</a><small>(austrian site payment in Euro)</small></li>
    <li><svg width="11" height="11"><circle cx="5.5" cy="5.5" r="5" fill="none" stroke="#aaa"/><path d="M.5 5.5h10M5.5.5c-3 3-3 7 0 10M5.5.5c3 3 3 7 0 10" fill="none" stroke="#aaa"/></svg><a href="#">http://www.wagen-wimpl.ch</a><small>(german site payment in Swiss Franken)</small></li>
  </ul>
</section>

<section class="panel" aria-label="Big flag shops" style="left:337px;top:448px;width:205px;height:263px">
  <div class="panel-band"></div>
  <div class="panel-mark"><span class="mark-text">tovRella</span></div>
  <ul class="links">
    <li><svg width="11" height="11"><circle cx="5.5" cy="5.5" r="5" fill="none" stroke="#aaa"/><path d="M.5 5.5h10M5.5.5c-3 3-3 7 0 10M5.5.5c3 3 3 7 0 10" fill="none" stroke="#aaa"/></svg><a href="#">http://www.tovrella.ne/</a><small>(english site payment in Euro)</small></li>
    <li><svg width="11" height="11"><circle cx="5.5" cy="5.5" r="5" fill="none" stroke="#aaa"/><path d="M.5 5.5h10M5.5.5c-3 3-3 7 0 10M5.5.5c3 3 3 7 0 10" fill="none" stroke="#aaa"/></svg><a href="#">http://fr.tovrella.net</a><small>(french site payment in Euro)</small></li>
    <li><svg width="11" height="11"><circle cx="5.5" cy="5.5" r="5" fill="none" stroke="#aaa"/><path d="M.5 5.5h10M5.5.5c-3 3-3 7 0 10M5.5.5c3 3 3 7 0 10" fill="none" stroke="#aaa"/></svg><a href="#">http://es.tovrella.net</a><small>(spanish site payment in Euro)</small></li>
    <li><svg width="11" height="11"><circle cx="5.5" cy="5.5" r="5" fill="none" stroke="#aaa"/><path d="M.5 5.5h10M5.5.5c-3 3-3 7 0 10M5.5.5c3 3 3 7 0 10" fill="none" stroke="#aaa"/></svg><a href="#">http://de.tovrella.net</a><small>(german site payment in Euro)</small></li>
    <li><svg width="11" height="11"><circle cx="5.5" cy="5.5" r="5" fill="none" stroke="#aaa"/><path d="M.5 5.5h10M5.5.5c-3 3-3 7 0 10M5.5.5c3 3 3 7 0 10" fill="none" stroke="#aaa"/></svg><a href="#">http://it.tovrella.net</a><small>(italian site payment in Euro)</small></li>
  </ul>
</section>

<section class="panel" aria-label="Car flags product page" style="left:337px;top:718px;width:205px;height:218px">
  <div class="panel-band"></div>
  <div class="panel-mark"><span class="mark-text gold">EnvoyPennon</span></div>
  <ul class="links">
    <li><svg width="11" height="11"><circle cx="5.5" cy="5.5" r="5" fill="none" stroke="#aaa"/><path d="M.5 5.5h10M5.5.5c-3 3-3 7 0 10M5.5.5c3 3 3 7 0 10" fill="none" stroke="#aaa"/></svg><a href="#">http://www.envoy-pennon.com</a><small>(english site)</small></li>
    <li><svg width="11" height="11"><circle cx="5.5" cy="5.5" r="5" fill="none" stroke="#aaa"/><path d="M.5 5.5h10M5.5.5c-3 3-3 7 0 10M5.5.5c3 3 3 7 0 10" fill="none" stroke="#aaa"/></svg><a href="#">http://fr.envoy-pennon.com</a><small>(french site)</small></li>
    <li><svg width="11" height="11"><circle cx="5.5" cy="5.5" r="5" fill="none" stroke="#aaa"/><path d="M.5 5.5h10M5.5.5c-3 3-3 7 0 10M5.5.5c3 3 3 7 0 10" fill="none" stroke="#aaa"/></svg><a href="#">http://es.envoy-pennon.com</a><small>(spanish site)</small></li>
    <li><svg width="11" height="11"><circle cx="5.5" cy="5.5" r="5" fill="none" stroke="#aaa"/><path d="M.5 5.5h10M5.5.5c-3 3-3 7 0 10M5.5.5c3 3 3 7 0 10" fill="none" stroke="#aaa"/></svg><a href="#">http://de.envoy-pennon.com</a><small>(german site)</small></li>
  </ul>
</section>

<aside class="newsletter">
  <div class="news-head">Newsletter</div>
  <p class="news-intro">Select Language and subscribe to our news-<br>letters using the form below</p>
  <div class="lang open">
    <svg class="flag" viewBox="0 0 11 8"><rect width="11" height="2.7" fill="#222"/><rect y="2.7" width="11" height="2.7" fill="#d22"/><rect y="5.4" width="11" height="2.6" fill="#f2c200"/></svg>
    Germany
    <svg class="chev" width="14" height="14"><circle cx="7" cy="7" r="6" fill="none" stroke="#8a7130"/><path d="M4 8.5l3-3 3 3" fill="none" stroke="#8a7130"/></svg>
    <span class="field-label" style="top:32px">Your Email</span>
    <span class="field" style="top:46px"></span>
    <span class="field-label" style="top:75px">Your Name</span>
    <span class="field" style="top:89px"></span>
    <a class="send" href="#">SEND</a>
  </div>
  <div class="lang">
    <svg class="flag" viewBox="0 0 11 8"><rect width="11" height="8" fill="#23408f"/><rect x="4.2" width="2.6" height="8" fill="#fff"/><rect y="2.7" width="11" height="2.6" fill="#fff"/><rect x="4.9" width="1.2" height="8" fill="#c8102e"/><rect y="3.4" width="11" height="1.2" fill="#c8102e"/></svg>
    United Kingdom
    <svg class="chev" width="14" height="14"><circle cx="7" cy="7" r="6" fill="none" stroke="#8a7130"/><path d="M4 6l3 3 3-3" fill="none" stroke="#8a7130"/></svg>
  </div>
  <div class="lang">
    <svg class="flag" viewBox="0 0 11 8"><rect width="3.7" height="8" fill="#2349a3"/><rect x="3.7" width="3.6" height="8" fill="#fff"/><rect x="7.3" width="3.7" height="8" fill="#e1262d"/></svg>
    France
    <svg class="chev" width="14" height="14"><circle cx="7" cy="7" r="6" fill="none" stroke="#8a7130"/><path d="M4 6l3 3 3-3" fill="none" stroke="#8a7130"/></svg>
  </div>
  <div class="lang">
    <svg class="flag" viewBox="0 0 11 8"><rect width="11" height="8" fill="#c8102e"/><rect y="2" width="11" height="4" fill="#f4c300"/></svg>
    Spain
    <svg class="chev" width="14" height="14"><circle cx="7" cy="7" r="6" fill="none" stroke="#8a7130"/><path d="M4 6l3 3 3-3" fill="none" stroke="#8a7130"/></svg>
  </div>
  <p class="news-note">We will save your personal data orem ipsum dolor sit amet, consectetuer adipiscing elit</p>
</aside>

<footer class="site-footer">
  <div class="foot-col" style="left:117px">
    <h3>MENU</h3>
    <ul><li>Home</li><li>Customer Service</li><li>Impressum</li><li>Site Map</li><li>Search Terms</li><li>Advanced Search</li><li>Orders and Returns</li><li>Contact Us</li><li>RSS</li></ul>
  </div>
  <span class="divider" style="left:265px"></span>
  <div class="foot-col" style="left:283px">
    <h3>USEFUL LINKS</h3>
    <ul><li>www.ridepennon.eu</li><li>www.ridepennon.net</li><li>www.ridepennant.co.uk</li><li>www.wagen-wimpel.net</li><li>www.wagen-banner.at</li><li>www.wagen-wimpl.ch</li></ul>
  </div>
  <span class="divider" style="left:430px"></span>
  <div class="foot-col" style="left:448px">
    <h3>CONTACTS</h3>
    <p>Tovrella GmbH<br>Am Lindenhang 14/3<br>73412 Haldenfeld<br>Germany</p>
    <p style="margin-top:18px">CEO, Geschäftsführer: Lorenzo Venter<br>Handelsregister: HRB 514372, Amtsgericht Stuttgart<br>Ust.-ID: DE902318476</p>
  </div>
  <div class="foot-col" style="left:606px;top:36px">
    <p>Phone 1&nbsp; : &nbsp;+49 (0) 711 - 48 27 19 310<br>Fax:&nbsp;&nbsp;&nbsp;&nbsp;&nbsp;&nbsp;&nbsp; : &nbsp;+49 (0) 711 - 48 27 19 319<br>VAT / TVA / UmSt. ID: DE902318476<br>Email&nbsp;&nbsp;&nbsp;&nbsp; : &nbsp;<u>info@tovrella.de</u></p>
  </div>
  <span class="foot-rule"></span>
  <p class="foot-legal">Terms and Conditions &nbsp;|&nbsp; Privacy Policy<br>© 2013 tovRella GmbH</p>
</footer>

</body>
</html>
```